Logo Tweak & Full Set of Stationery

We need a redesign / tweaking of Logo for rebranding of our company. We are Australia's largest installer of commercial fencing and high security infrastructure. We also have divisions in security and civil works (infrastrucuture).

We would like to see designs that incorporate black, white & blue. Revamp of current Diamond Logo (including HC) would be ideal but open to all ideas.

Design needs to portray a highly professional & corporate image.

Required:
- Tweak / Redesign of Logo
- Letterhead
- email Signature
- Business Cards
- Presentation Folder

Address fields should be interchangeable to accomodate multiple locations.

Website: www.harvillecorp.com.au
Updates

Due to short turn around time for project - Fee increased to $500 AUD Guaranteed

Thanks

Designs are looking good
I have emailed those submitted thus far to the board to start short listing.

Please do not take offence if your design is eliminated as part of this process  - there are so many great concepts and if is difficult to pick between them.

Thanks
Dustin

Target Market(s)

Tier 1 / 2 Builders (ie.. Brick Arch Peter Farley) and Government related bodies

Industry/Entity Type

Security

Requirements
Must have
• Company Name: Harville Corp

Tag Line: Fencing * Security * Civil

Logo

```html
<!DOCTYPE html>
<html lang="en">
<head>
<meta charset="utf-8">
<title>Harville Corp – Business Card</title>
<link rel="stylesheet" href="https://fonts.googleapis.com/css2?family=Cinzel:wght@400;600&display=swap">
<style>
  :root {
    --page: #ffffff;
    --card-dark: #000000;
    --brand-blue: #29abe2;
    --brand-grey: #c8c8c8;
    --ink-light: #ffffff;
    --ink-dark: #0a0a0a;
  }
  * { margin: 0; padding: 0; box-sizing: border-box; }
  html, body {
    width: 1200px;
    height: 900px;
    overflow: hidden;
    background: var(--page);
    font-family: "Cinzel", "Times New Roman", serif;
  }
  .stage { position: relative; width: 1200px; height: 900px; }
  .card {
    position: absolute;
    left: 282px;
    width: 638px;
    height: 398px;
  }
  .card--front { top: 28px; background: var(--card-dark); color: var(--ink-light); }
  .card--back { top: 464px; background: var(--brand-blue); color: var(--ink-dark); }

  .centered { position: absolute; left: 0; right: 0; text-align: center; }

  .brand-mark {
    position: absolute;
    left: 294px;
    top: 86px;
    width: 50px;
    height: 50px;
    background: var(--brand-blue);
  }
  .brand-name {
    top: 196px;
    font-size: 46px;
    line-height: 1;
    font-weight: 400;
    color: var(--brand-blue);
    letter-spacing: 1px;
  }
  .brand-rule {
    position: absolute;
    left: 112px;
    width: 396px;
    top: 250px;
    height: 2px;
    background: var(--ink-light);
  }
  .brand-entity {
    top: 263px;
    font-size: 20px;
    line-height: 1;
    letter-spacing: 9px;
    color: var(--ink-light);
  }
  .tagline {
    top: 332px;
    font-size: 22px;
    letter-spacing: 3px;
    color: var(--brand-blue);
  }

  .contact-name { top: 96px; font-size: 24px; letter-spacing: 2px; color: var(--ink-light); }
  .contact-title { top: 130px; font-size: 19px; letter-spacing: 1.5px; color: var(--ink-dark); }
  .contact-mobile { top: 162px; font-size: 19px; letter-spacing: 1.5px; color: var(--ink-dark); }

  .detail {
    position: absolute;
    font-size: 16px;
    letter-spacing: 1.5px;
    color: var(--ink-dark);
  }
  .detail--phone { left: 40px; top: 254px; }
  .detail--email { left: 394px; top: 254px; }
  .detail--freecall { left: 40px; top: 298px; }
  .detail--fax { left: 394px; top: 298px; }

  .website {
    top: 348px;
    font-size: 16px;
    letter-spacing: 3px;
    color: var(--ink-light);
  }
</style>
</head>
<body>
<main class="stage">
  <section class="card card--front">
    <div class="brand-mark"></div>
    <h1 class="centered brand-name">Harville Corp</h1>
    <div class="brand-rule"></div>
    <p class="centered brand-entity">Australia Pty Ltd</p>
    <p class="centered tagline">Fencing // Security // Civil</p>
  </section>

  <section class="card card--back">
    <p class="centered contact-name">Dustin Keane</p>
    <p class="centered contact-title">Chief Financial Officer</p>
    <p class="centered contact-mobile">Mobile: 9400 555 018</p>

    <p class="detail detail--phone">Phone: 9400 555 018</p>
    <p class="detail detail--email">E-Mail: 9400 555 018</p>
    <p class="detail detail--freecall">Free Call: 9400 555 018</p>
    <p class="detail detail--fax">Fax: 9400 555 018</p>

    <p class="centered website">www.harvillecorp.com.au</p>
  </section>
</main>
</body>
</html>
```